REDESIGN COUPLE PAGES FOR VIMLO VIDEO ADS

PLEASE REDESIGN THIS PAGE FOR ME:
http://pageframequarry.com/kq/rudy/vimlo/pricing.html
I need it to be easy to read for the end user so the customer knows exactly what he will be getting. Make an emphasis on the subscription as the most popular item....and also the price per video format should be emphasized too.

Target Market(s)

B2B

Industry/Entity Type

Video Production

Number of Pages Required

3 page

Colors

Designer to choose colors to be used in the design.

Requirements
Must have
• PLEASE REDESIGN THIS PAGE FOR ME:
• http://pageframequarry.com/kq/rudy/vimlo/pricing.html
• I need it to be easy to read for the end user so the customer knows exactly what he will be getting. Make an emphasis on the subscription as the most popular item....and also the price per video format should be emphasized too.
Nice to have
Should not have

```html
<!DOCTYPE html>
<html lang="en">
<head>
<meta charset="utf-8">
<title>VIMLO Pricing</title>
<link href="https://fonts.googleapis.com/css2?family=Lato:wght@400;700;900&display=swap" rel="stylesheet">
<style>
:root{
  --navy:#131c2e;
  --blue:#3a7fdc;
  --blue-btn:#2f74d8;
  --sky:#5cc3f1;
  --red:#e0463a;
  --ink:#1e2430;
  --muted:#5b6372;
  --soft:#8a909b;
  --line:#eceef1;
  --band:#f2f3f5;
  --white:#ffffff;
}
*{box-sizing:border-box;margin:0;padding:0}
html,body{width:993px;height:1200px;overflow:hidden;background:var(--white);font-family:'Lato',sans-serif;color:var(--ink)}
.site-nav{height:57px;background:var(--navy);position:relative;color:var(--white)}
.brand{position:absolute;left:11px;top:17px;font-weight:900;font-size:20px;letter-spacing:3px;line-height:22px;display:flex;align-items:center;gap:6px}
.brand i{display:inline-block;width:10px;height:10px;background:var(--white)}
.nav-links{position:absolute;left:302px;top:0;height:57px;display:flex;align-items:center;gap:17px;list-style:none;font-size:11.6px}
.nav-links .active{color:#56a7f2}
.login{position:absolute;left:872px;top:21px;font-size:11.6px}
.signup{position:absolute;left:920px;top:13px;width:61px;height:29px;background:var(--blue-btn);border:1px solid #6aa6f0;border-radius:2px;font-size:11.6px;display:flex;align-items:center;justify-content:center}

.pricing{position:absolute;left:68px;top:89px;width:857px;height:1067px;background:var(--white);border-radius:9px;box-shadow:0 2px 14px rgba(20,30,50,.08);overflow:hidden}
.grid{display:grid;grid-template-columns:152px 143px 139px 141px 139px 143px}
.plans{height:175px}
.intro{text-align:center;padding-top:26px;border-right:1px solid var(--line)}
.intro h1{font-size:17.5px;line-height:23.5px;font-weight:400;color:#111}
.intro p{margin-top:9px;font-size:11.5px;line-height:19px;color:var(--soft);letter-spacing:.3px}
.plan{text-align:center;position:relative;border-right:1px solid var(--line)}
.plan:last-child{border-right:0}
.price{position:absolute;top:22px;left:0;right:0;font-size:29px;font-weight:900;color:var(--blue);line-height:34px}
.price sup{font-size:12px;font-weight:400;color:var(--soft);vertical-align:top;position:relative;top:2px;margin-right:3px}
.plan h2{position:absolute;top:66px;left:0;right:0;font-size:10px;font-weight:700}
.plan .desc{position:absolute;top:82px;left:0;right:0;font-size:9.8px;line-height:16px;color:var(--muted)}
.buy{position:absolute;top:128px;left:50%;margin-left:-48px;width:96px;height:27px;border-radius:14px;background:var(--blue-btn);color:var(--white);font-size:8.6px;letter-spacing:.6px;display:flex;align-items:center;justify-content:center}
.plan.featured{background:var(--blue);color:var(--white);border-right:0}
.plan.featured .price,.plan.featured sup,.plan.featured .desc{color:var(--white)}
.plan.featured .buy{background:var(--sky)}
.band{height:36px;background:var(--band);font-size:10px;display:flex;align-items:center;padding-left:16px;color:#222}
.row{border-bottom:1px solid var(--line);height:43px}
.row.sm{height:41px}
.row.tall{height:57px;border-bottom:0}
.row>div{display:flex;align-items:center;justify-content:center;font-size:10px;font-weight:700;border-right:1px solid var(--line)}
.row>div:last-child{border-right:0}
.row>.label{justify-content:flex-start;padding-left:16px;font-weight:400;color:var(--muted);line-height:17px}
.ic{width:11px;height:11px}
</style>
</head>
<body>
<svg width="0" height="0" style="position:absolute">
  <defs>
    <symbol id="yes" viewBox="0 0 12 12"><circle cx="6" cy="6" r="6" fill="#3a7fdc"/><path d="M3.3 6.2l1.8 1.8 3.6-3.7" fill="none" stroke="#fff" stroke-width="1.5" stroke-linecap="round" stroke-linejoin="round"/></symbol>
    <symbol id="no" viewBox="0 0 12 12"><circle cx="6" cy="6" r="6" fill="#e0463a"/><path d="M4 4l4 4M8 4l-4 4" stroke="#fff" stroke-width="1.5" stroke-linecap="round"/></symbol>
  </defs>
</svg>

<header class="site-nav">
  <div class="brand"><i></i>VIMLO</div>
  <ul class="nav-links">
    <li>Home</li><li>How It Works</li><li>Examples</li><li>FAQ</li><li>Contact Us</li><li class="active">Pricing</li><li>Calendar</li>
  </ul>
  <span class="login">Log In</span>
  <span class="signup">Sign Up</span>
</header>

<main class="pricing">
  <div class="grid plans">
    <div class="intro"><h1>No<br>Hidden<br>Charges</h1><p>CHOOSE<br>YOUR DEALS</p></div>
    <div class="plan"><div class="price"><sup>$</sup>37</div><h2>Al A Carte</h2><div class="desc">As Needed Basis</div><span class="buy">BUY NOW</span></div>
    <div class="plan featured"><div class="price"><sup>$</sup>16</div><h2>Subscription</h2><div class="desc">New Video<br>Ads Monthly</div><span class="buy">BUY NOW</span></div>
    <div class="plan"><div class="price"><sup>$</sup>14</div><h2>Holiday Pkg</h2><div class="desc">17 Holiday<br>Themed Videos</div><span class="buy">BUY NOW</span></div>
    <div class="plan"><div class="price"><sup>$</sup>18</div><h2>Season Pkg</h2><div class="desc">4 Seasonal<br>Themed Videos</div><span class="buy">BUY NOW</span></div>
    <div class="plan"><div class="price"><sup>$</sup>10</div><h2>Social Media Calendar</h2><div class="desc">Daily Videos For<br>Your Social Media</div><span class="buy">BUY NOW</span></div>
  </div>

  <div class="band">Features</div>

  <div class="grid row"><div class="label">Videos Included</div><div>Custom</div><div>Custom</div><div>17</div><div>4</div><div>30</div></div>
  <div class="grid row"><div class="label">Cost Per Video Format</div><div>Starts @ $37/Video</div><div>Starts @ $16/Video</div><div>$14/Video</div><div>$18/Video</div><div>$10/Video</div></div>
  <div class="grid row"><div class="label">Delivery Speed</div><div>24 Hours</div><div>24 Hours</div><div>3-5 Days</div><div>3-5 Days</div><div>Prior To Next Month</div></div>
  <div class="grid row"><div class="label">Revisions</div><div>Unlimited</div><div>Unlimited</div><div>Unlimited</div><div>Unlimited</div><div>Unlimited</div></div>
  <div class="grid row"><div class="label">Final File Formats</div><div>Mp4 Full Hd 1080P</div><div>Mp4 Full Hd 1080P</div><div>Mp4 Full Hd 1080P</div><div>Mp4 Full Hd 1080P</div><div>Mp4 Full Hd 1080P</div></div>
  <div class="grid row"><div class="label">Wide Screen Video Format</div><div><svg class="ic"><use href="#yes"/></svg></div><div><svg class="ic"><use href="#yes"/></svg></div><div><svg class="ic"><use href="#yes"/></svg></div><div><svg class="ic"><use href="#yes"/></svg></div><div><svg class="ic"><use href="#no"/></svg></div></div>
  <div class="grid row"><div class="label">Large Square Video Format</div><div><svg class="ic"><use href="#yes"/></svg></div><div><svg class="ic"><use href="#yes"/></svg></div><div><svg class="ic"><use href="#yes"/></svg></div><div><svg class="ic"><use href="#yes"/></svg></div><div><svg class="ic"><use href="#yes"/></svg></div></div>
  <div class="grid row"><div class="label">Vertical Video Format</div><div><svg class="ic"><use href="#yes"/></svg></div><div><svg class="ic"><use href="#yes"/></svg></div><div><svg class="ic"><use href="#yes"/></svg></div><div><svg class="ic"><use href="#yes"/></svg></div><div><svg class="ic"><use href="#no"/></svg></div></div>
  <div class="grid row"><div class="label">Page Cover Video Format</div><div><svg class="ic"><use href="#yes"/></svg></div><div><svg class="ic"><use href="#yes"/></svg></div><div><svg class="ic"><use href="#yes"/></svg></div><div><svg class="ic"><use href="#yes"/></svg></div><div><svg class="ic"><use href="#no"/></svg></div></div>
  <div class="grid row"><div class="label">Holiday Theme Video</div><div>Optional</div><div><svg class="ic"><use href="#yes"/></svg></div><div><svg class="ic"><use href="#yes"/></svg></div><div><svg class="ic"><use href="#no"/></svg></div><div><svg class="ic"><use href="#yes"/></svg></div></div>
  <div class="grid row"><div class="label">Seasonal Theme Video</div><div>Optional</div><div><svg class="ic"><use href="#yes"/></svg></div><div><svg class="ic"><use href="#no"/></svg></div><div><svg class="ic"><use href="#yes"/></svg></div><div><svg class="ic"><use href="#yes"/></svg></div></div>
  <div class="grid row"><div class="label">Content Done For You</div><div><svg class="ic"><use href="#yes"/></svg></div><div><svg class="ic"><use href="#yes"/></svg></div><div><svg class="ic"><use href="#yes"/></svg></div><div><svg class="ic"><use href="#yes"/></svg></div><div><svg class="ic"><use href="#yes"/></svg></div></div>
  <div class="grid row sm"><div class="label">Full Branding In Video</div><div><svg class="ic"><use href="#yes"/></svg></div><div><svg class="ic"><use href="#yes"/></svg></div><div><svg class="ic"><use href="#yes"/></svg></div><div><svg class="ic"><use href="#yes"/></svg></div><div><svg class="ic"><use href="#yes"/></svg></div></div>
  <div class="grid row sm"><div class="label">Full Copyright Ownership</div><div><svg class="ic"><use href="#yes"/></svg></div><div><svg class="ic"><use href="#yes"/></svg></div><div><svg class="ic"><use href="#yes"/></svg></div><div><svg class="ic"><use href="#yes"/></svg></div><div><svg class="ic"><use href="#yes"/></svg></div></div>
  <div class="grid row sm"><div class="label">Full Reselling Rights</div><div><svg class="ic"><use href="#yes"/></svg></div><div><svg class="ic"><use href="#yes"/></svg></div><div><svg class="ic"><use href="#yes"/></svg></div><div><svg class="ic"><use href="#yes"/></svg></div><div><svg class="ic"><use href="#yes"/></svg></div></div>
  <div class="grid row sm"><div class="label">Premium Video Clips</div><div><svg class="ic"><use href="#yes"/></svg></div><div><svg class="ic"><use href="#yes"/></svg></div><div><svg class="ic"><use href="#yes"/></svg></div><div><svg class="ic"><use href="#yes"/></svg></div><div><svg class="ic"><use href="#yes"/></svg></div></div>
  <div class="grid row sm"><div class="label">Use My Images</div><div><svg class="ic"><use href="#yes"/></svg></div><div><svg class="ic"><use href="#yes"/></svg></div><div><svg class="ic"><use href="#yes"/></svg></div><div><svg class="ic"><use href="#yes"/></svg></div><div><svg class="ic"><use href="#yes"/></svg></div></div>
  <div class="grid row sm"><div class="label">Use My Video Footage</div><div><svg class="ic"><use href="#yes"/></svg></div><div><svg class="ic"><use href="#yes"/></svg></div><div><svg class="ic"><use href="#yes"/></svg></div><div><svg class="ic"><use href="#yes"/></svg></div><div><svg class="ic"><use href="#yes"/></svg></div></div>
  <div class="grid row sm"><div class="label">Use My Background Music</div><div><svg class="ic"><use href="#yes"/></svg></div><div><svg class="ic"><use href="#yes"/></svg></div><div><svg class="ic"><use href="#yes"/></svg></div><div><svg class="ic"><use href="#yes"/></svg></div><div><svg class="ic"><use href="#yes"/></svg></div></div>
  <div class="grid row tall"><div class="label">Fully Licensed<br>Background Music</div><div><svg class="ic"><use href="#yes"/></svg></div><div><svg class="ic"><use href="#yes"/></svg></div><div><svg class="ic"><use href="#yes"/></svg></div><div><svg class="ic"><use href="#yes"/></svg></div><div><svg class="ic"><use href="#yes"/></svg></div></div>
</main>
</body>
</html>
```